Business Cards for Logistics Company

Looking to update Business Card Design.
Logo is attached. Blue background is not a part of the logo, you can remove it in layers.

Company: Harbor Crest Freightways
Industry: Logistics, Container Shipping

Address:
418 Willow Bend Ave
Bayonne NJ 07419

Phones:
p. 201-555-0143
f. 201-555-0178
c. very by person's name

Website: www.hcfroute.example

Design has to include person's name and position.
OLD Design is included.

B2B

Business

Card Size (non standard): 1039 x 697 pixels, 300dpi
Template is attached.

Font styles to use
Serif
Sans Serif

```html
<!DOCTYPE html>
<html lang="en">
<head>
<meta charset="utf-8">
<title>Harbor Crest Freightways – Business Card</title>
<link href="https://fonts.googleapis.com/css2?family=Share+Tech+Mono&family=Oxygen:wght@400;700&display=swap" rel="stylesheet">
<style>
  :root {
    --navy: #020066;
    --sky: #6f8fc9;
    --white: #ffffff;
    --page: #ffffff;
    --mono: "Share Tech Mono", monospace;
    --sans: "Oxygen", sans-serif;
  }
  * { box-sizing: border-box; margin: 0; padding: 0; }
  html, body { width: 1200px; height: 1000px; overflow: hidden; background: var(--page); }
  .canvas { position: relative; width: 1200px; height: 1000px; }

  .card {
    position: absolute;
    width: 520px;
    height: 348px;
    background: var(--navy);
    color: var(--white);
    overflow: hidden;
  }
  .card--front { left: 340px; top: 120px; }
  .card--back  { left: 340px; top: 530px; }

  /* Back side */
  .tagline-band {
    position: absolute; left: 0; top: 24px; width: 100%; height: 58px;
    background: var(--sky); text-align: center; padding-top: 7px;
  }
  .tagline {
    font-family: var(--mono); font-variant: small-caps;
    font-size: 21px; letter-spacing: 2.5px;
  }
  .services {
    font-family: var(--mono); font-variant: small-caps;
    font-size: 11.5px; letter-spacing: 1.2px; margin-top: 4px;
  }
  .brand-lockup {
    position: absolute; left: 116px; top: 138px;
    display: flex; align-items: center; gap: 14px;
  }
  .brand-mark { width: 64px; height: 64px; background: var(--sky); }
  .brand-name {
    font-family: var(--sans); font-size: 17px; letter-spacing: 2px;
    line-height: 1.15; text-transform: uppercase; width: 190px;
  }
  .web-band {
    position: absolute; left: 0; top: 296px; width: 100%; height: 28px;
    background: var(--sky);
  }
  .web {
    position: absolute; left: 200px; top: 5px;
    font-family: var(--mono); font-size: 15px; letter-spacing: 2px; text-transform: uppercase;
  }

  /* Front side */
  .panel-contact { position: absolute; left: 0; top: 0; width: 236px; height: 100%; background: var(--navy); }
  .panel-person  { position: absolute; left: 236px; top: 0; right: 0; height: 100%; background: var(--sky); }

  .front-lockup {
    position: absolute; left: 30px; top: 50px;
    display: flex; align-items: center; gap: 10px;
  }
  .front-lockup .brand-mark { width: 46px; height: 46px; }
  .front-lockup .brand-name { font-size: 12.5px; width: 140px; letter-spacing: 1.5px; }

  .contacts { position: absolute; left: 22px; top: 150px; list-style: none; }
  .contacts li {
    display: flex; align-items: center; gap: 7px;
    font-family: var(--mono); font-size: 14px; letter-spacing: 1px; line-height: 20px;
  }
  .contacts svg { width: 13px; height: 13px; flex: none; }
  .contacts .email { font-size: 11.5px; text-transform: uppercase; }

  .person { position: absolute; left: 30px; top: 52px; }
  .person-name {
    font-family: var(--mono); font-variant: small-caps; font-weight: 700;
    font-size: 21px; letter-spacing: 2px;
  }
  .person-role {
    font-family: var(--mono); font-variant: small-caps;
    font-size: 12px; letter-spacing: 1.5px; margin-top: 2px; padding-left: 40px;
  }
  .address {
    position: absolute; left: 30px; top: 150px;
    font-family: var(--mono); font-variant: small-caps; font-style: normal;
    font-size: 19px; letter-spacing: 3px; line-height: 24px;
  }
</style>
</head>
<body>
<main class="canvas">

  <section class="card card--front" aria-label="Business card front">
    <div class="panel-contact">
      <div class="front-lockup">
        <span class="brand-mark"></span>
        <span class="brand-name">Harbor Crest Freightways</span>
      </div>
      <ul class="contacts">
        <li>
          <svg viewBox="0 0 16 16" aria-hidden="true"><path d="M3 2h3l1 4-2 1a9 9 0 0 0 4 4l1-2 4 1v3a1 1 0 0 1-1 1A13 13 0 0 1 2 3a1 1 0 0 1 1-1z" fill="#fff"/></svg>
          201-555-0143
        </li>
        <li>
          <svg viewBox="0 0 16 16" aria-hidden="true"><rect x="3" y="1" width="10" height="5" fill="none" stroke="#fff" stroke-width="1.5"/><rect x="1" y="6" width="14" height="8" rx="1" fill="#fff"/></svg>
          201-555-0178
        </li>
        <li>
          <svg viewBox="0 0 16 16" aria-hidden="true"><rect x="4" y="1" width="8" height="14" rx="1.5" fill="none" stroke="#fff" stroke-width="1.5"/><circle cx="8" cy="12.5" r="1" fill="#fff"/></svg>
          646-555-0192
        </li>
        <li class="email">
          <svg viewBox="0 0 16 16" aria-hidden="true"><rect x="1" y="3" width="14" height="10" fill="none" stroke="#fff" stroke-width="1.5"/><path d="M1 3l7 6 7-6" fill="none" stroke="#fff" stroke-width="1.5"/></svg>
          info@hcfroute.example
        </li>
      </ul>
    </div>
    <div class="panel-person">
      <div class="person">
        <p class="person-name">Dmitri Varenko</p>
        <p class="person-role">General Manager</p>
      </div>
      <address class="address">
        Harbor Crest<br>
        Freightways Inc<br>
        418 Willow Bend Ave<br>
        Bayonne NJ 07419
      </address>
    </div>
  </section>

  <section class="card card--back" aria-label="Business card back">
    <div class="tagline-band">
      <p class="tagline">International Transportation Solutions</p>
      <p class="services">Ocean &amp; Air Freight | Loading &amp; Storage | Multimodal Transport</p>
    </div>
    <div class="brand-lockup">
      <span class="brand-mark"></span>
      <span class="brand-name">Harbor Crest Freightways</span>
    </div>
    <div class="web-band">
      <span class="web">hcfroute.example</span>
    </div>
  </section>

</main>
</body>
</html>
```